Mental Health & Addiction Podcast Art

Project: Podcast Cover Art / Visual Identity
Podcast Name: The Mending Path
Focus: Recovery from substance use and mental health
Objectives
Create compelling podcast artwork that:
Reflects the themes of hope, healing, and personal growth
Establishes credibility and professionalism
Appeals to individuals seeking recovery resources and support
Maintains strong brand consistency with Larkspur Wellness
Brand Integration Requirements
Logo incorporation: Integrate an element from the Larkspur Wellness Logo—potentially an abstract or partial use of the sun motif
Flexibility: Open to creative interpretations (e.g., sun rays as background texture, sunrise gradient, partial sun as a design accent)
Mandatory: Must adhere to existing Larkspur Wellness brand guidelines (approved color palette, typography, and visual style)

Target Market(s)

United states, people with addiction and mental health disorders.

Industry/Entity Type

Wellness

Font styles to use
Other font styles liked:
• See Brand Guide

Requirements
Must have
• Match brand guide, in corporate elements of the Larkspur Wellness Logo icon

```html
<!DOCTYPE html>
<html lang="en">
<head>
<meta charset="utf-8">
<title>The Mending Path – Podcast Cover Options</title>
<link rel="stylesheet" href="https://fonts.googleapis.com/css2?family=IBM+Plex+Sans:wght@300;400;600&family=IBM+Plex+Sans+Condensed:wght@400&family=Playfair+Display:ital,wght@1,700;1,800&display=swap">
<style>
  :root {
    --teal: #05465f;
    --teal-deep: #0a3148;
    --steel: #4f87a3;
    --amber: #fbab0a;
    --white: #ffffff;
    --page: #ffffff;
  }
  * { box-sizing: border-box; margin: 0; padding: 0; }
  html, body { width: 1200px; height: 611px; overflow: hidden; background: var(--page); }
  .canvas { position: relative; width: 1200px; height: 611px; }

  .cover {
    position: absolute; top: 21px; width: 569px; height: 569px;
    background: var(--teal); overflow: hidden;
  }
  .cover--centered { left: 18px; }
  .cover--editorial { left: 605px; }

  /* Centered cover */
  .sun-motif {
    position: absolute; left: 44px; top: 0; width: 480px; height: 440px;
    background: radial-gradient(circle 210px at 50% 50%,
      rgba(251,171,10,0.9) 0%,
      rgba(251,171,10,0.55) 30%,
      rgba(251,171,10,0.2) 62%,
      rgba(251,171,10,0) 100%);
  }
  .title-stack {
    position: absolute; left: 0; right: 0; top: 268px;
    text-align: center; color: var(--white);
    font-family: "Playfair Display", Georgia, serif; font-style: italic; font-weight: 800;
    font-size: 60px; line-height: 56px; letter-spacing: -1px;
  }
  .title-stack span { display: block; }
  .tagline-pill {
    position: absolute; left: 131px; top: 458px; width: 306px; height: 25px;
    border-radius: 13px; background: var(--amber); color: var(--teal-deep);
    font-family: "IBM Plex Sans Condensed", "Arial Narrow", sans-serif; font-size: 13.5px;
    letter-spacing: -0.3px; display: flex; align-items: center; justify-content: center;
  }
  .brand {
    position: absolute; display: flex; align-items: center; gap: 5px;
    font-family: "IBM Plex Sans", Arial, sans-serif; font-weight: 400; font-size: 13px;
    color: var(--white); text-transform: uppercase; white-space: nowrap;
  }
  .brand__dot {
    width: 20px; height: 20px; border-radius: 50%; border: 1.5px solid var(--white);
  }
  .cover--centered .brand { left: 50%; top: 514px; transform: translateX(-50%); }

  /* Editorial cover */
  .cover--editorial svg.geometry { position: absolute; inset: 0; }
  .cover--editorial .brand { left: 50%; top: 57px; transform: translateX(-50%); font-size: 15px; }
  .cover--editorial .brand__dot { width: 26px; height: 26px; }
  .headline {
    position: absolute; left: 44px; top: 186px; color: var(--white);
    font-family: "IBM Plex Sans", Arial, sans-serif; font-weight: 300;
  }
  .headline__line { display: block; font-size: 74px; line-height: 74px; letter-spacing: 1px; }
  .headline__accent {
    display: block; color: var(--amber);
    font-family: "Playfair Display", Georgia, serif; font-style: italic; font-weight: 800;
    font-size: 96px; line-height: 82px; letter-spacing: -2px; margin-left: -2px;
  }
  .subtitle {
    position: absolute; left: 52px; top: 441px; padding-left: 12px;
    border-left: 3px solid var(--amber); color: var(--white);
    font-family: "IBM Plex Sans", Arial, sans-serif; font-weight: 300;
    font-size: 15.5px; line-height: 19px;
  }
  .subtitle strong { font-weight: 600; }
</style>
</head>
<body>
<main class="canvas">

  <section class="cover cover--centered" aria-label="The Mending Path cover, centered version">
    <div class="sun-motif" role="img" aria-label="Warm amber sun motif from the Larkspur Wellness brand"></div>
    <h1 class="title-stack"><span>The</span><span>Mending</span><span>Path</span></h1>
    <p class="tagline-pill">Recovery from substance use and mental health</p>
    <div class="brand" aria-label="Larkspur Wellness Logo"><span class="brand__dot"></span>Larkspur Wellness</div>
  </section>

  <section class="cover cover--editorial" aria-label="The Mending Path cover, editorial version">
    <svg class="geometry" width="569" height="569" viewBox="0 0 569 569" aria-hidden="true">
      <polygon points="0,0 171,0 0,193" fill="var(--teal-deep)"/>
      <polygon points="569,254 569,552 303,552" fill="var(--steel)"/>
      <rect x="0" y="552" width="569" height="17" fill="var(--amber)"/>
    </svg>
    <div class="brand" aria-label="Larkspur Wellness Logo"><span class="brand__dot"></span>Larkspur Wellness</div>
    <h2 class="headline">
      <span class="headline__line">THE</span>
      <span class="headline__accent">Mending</span>
      <span class="headline__line">PATH</span>
    </h2>
    <p class="subtitle"><strong>Recovery</strong> from substance use<br>and mental health</p>
  </section>

</main>
</body>
</html>
```